Velisto Events Business Card

We need a business cards that stands out to our clients. We are company who targets prestige clients to spend money with us on experiences, so our image needs to be prestige
Target Market(s)
Corporate
Contact Information for Business Card
There will be four different names on the business cards
Dana Morrowby
Director
O: 02 5147 3086
M: 0451 692 038
E: info@velistoevents.example.au
Facebook: @velistoevents
Instagram: velistoevents
www.velistoevents.example.au
Nathaniel Morrowby
Director
O: 02 5147 3086
M: 0467 215 904
Facebook: @velistoevents
Instagram: velistoevents
www.velistoevents.example.au
Teodor Vinkel
Director
O: 02 5147 3086
M: 0478 903 527
Facebook: @velistoevents
Instagram: velistoevents
www.velistoevents.example.au
Mabel Hartung
Director
O: 02 5147 3086
Facebook: @velistoevents
Instagram: velistoevents
www.velistoevents.example.au
Colors
Designer to choose colors to be used in the design.
Look and feel

```html
<!DOCTYPE html>
<html lang="en">
<head>
<meta charset="utf-8">
<title>Velisto Events — Business Card</title>
<link href="https://fonts.googleapis.com/css2?family=Cinzel:wght@500&family=Montserrat:wght@500&display=swap" rel="stylesheet">
<style>
  :root {
    --page: #0a0a0b;
    --card: #111112;
    --card-edge: #1c1c1e;
    --gold: #c9a24e;
  }
  * { margin: 0; padding: 0; box-sizing: border-box; }
  html, body {
    width: 1200px;
    height: 1200px;
    overflow: hidden;
    background: var(--page);
  }
  .sheet {
    width: 1200px;
    height: 1200px;
    display: flex;
    flex-direction: column;
    align-items: center;
    justify-content: center;
    gap: 64px;
  }
  .card {
    position: relative;
    width: 700px;
    height: 400px;
    background: var(--card);
    border: 1px solid var(--card-edge);
    box-shadow: 0 20px 50px rgba(0,0,0,0.6);
  }
  .card-front {
    display: flex;
    flex-direction: column;
    align-items: center;
    justify-content: center;
  }
  .brand-dot {
    width: 14px;
    height: 14px;
    border-radius: 50%;
    background: var(--gold);
    margin-bottom: 28px;
  }
  .wordmark {
    font-family: "Cinzel", serif;
    font-weight: 500;
    color: var(--gold);
    font-size: 44px;
    letter-spacing: 0.22em;
    padding-left: 0.22em;
    line-height: 1;
  }
  .wordmark-sub {
    font-family: "Cinzel", serif;
    font-weight: 500;
    color: var(--gold);
    font-size: 18px;
    letter-spacing: 0.42em;
    padding-left: 0.42em;
    margin-top: 14px;
  }
  .back-mark {
    position: absolute;
    top: 34px;
    right: 30px;
    font-family: "Cinzel", serif;
    font-weight: 500;
    color: var(--gold);
    font-size: 14px;
    letter-spacing: 0.2em;
  }
  .contact {
    position: absolute;
    left: 26px;
    bottom: 26px;
    color: var(--gold);
    font-family: "Montserrat", sans-serif;
    font-weight: 500;
  }
  .contact-name {
    font-family: "Cinzel", serif;
    font-size: 17px;
    letter-spacing: 0.24em;
    line-height: 1.2;
  }
  .contact-title {
    font-size: 10px;
    letter-spacing: 0.18em;
    text-transform: uppercase;
    margin: 4px 0 14px;
  }
  .contact-line {
    font-size: 10px;
    letter-spacing: 0.02em;
    text-transform: uppercase;
    line-height: 1.2;
    margin-bottom: 9px;
  }
  .contact-line:last-child { margin-bottom: 0; }
</style>
</head>
<body>
  <main class="sheet">
    <section class="card card-front" aria-label="Card front">
      <div class="brand-dot"></div>
      <div class="wordmark">VELISTO</div>
      <div class="wordmark-sub">EVENTS</div>
    </section>

    <section class="card card-back" aria-label="Card back">
      <div class="back-mark">VELISTO</div>
      <div class="contact">
        <p class="contact-name">DANA MORROWBY</p>
        <p class="contact-title">Director</p>
        <p class="contact-line">O: 02 5147 3086</p>
        <p class="contact-line">M: 0451 692 038</p>
        <p class="contact-line">E: info@velistoevents.example.au</p>
        <p class="contact-line">Facebook: @velistoevents</p>
        <p class="contact-line">Instagram: velistoevents</p>
        <p class="contact-line">www.velistoevents.example.au</p>
      </div>
    </section>
  </main>
</body>
</html>
```